Marquen Premium Men's Shaving Cream Product Label . Cream packaged in a Amber Jar/Black Top Cap.

Please include information ( see Marquen design Template attachment) designed on a Round Top cap. Label Diameter: 3.125" NOTE: Design this First,
Wrap Around Label: 11.3125 x 0.875" (w x h): NOTE: Required latter after selection of Final Design Selection.
Shave Cream packaged in an 8oz Low Profile Amber Jar/Black Top Cap.
Thanks

Target Market(s)

Prime Target-Men Ages 20yrs-65yrs+ and Women 20yrs-65yrs+( they purchase ovr 55% of these Mens care products for partner/spouse/friend.

Industry/Entity Type

Personel Care/Cosmetics/NaturalHealthcare

Other font styles liked:
• At this stage if you would like to submi a desigh that would include both a Top Label and your Wrap-around label on a Amber jar/black top lid. It would be helpful to see how it would look complete. Thanks . Please refer to the updated design Graphic Template for copy and layout . Questions? Let me know. Thanks.Please now use QUILLSTONE on label designs. Thanks! Please see image attachment for added Tree Image Vector that can be added to your design instead of the Original Tree Image .

Requirements
Must have
• Look and Feel of a Quality/Premium Mens Skincare Brand with a Masculine feel but attractive to women as well ( not Macho!).Think Unisex with a Male slant.
Nice to have
• Premium/Quality/Natural Skincare & Bodycare Brand
Should not have
• Not Macho. No Cartoony or Barber Tools/Bearded Men Images. Too gimicky and over-hyped!

```html
<!DOCTYPE html>
<html lang="en">
<head>
<meta charset="utf-8">
<title>Marquen Shaving Cream – Top Cap Label</title>
<link rel="stylesheet" href="https://fonts.googleapis.com/css2?family=Inter:wght@400;600;700;800&display=swap">
<style>
  :root {
    --page: #ffffff;
    --sky-top: #86a6da;
    --sky-mid: #7482c4;
    --sky-low: #6a6cb2;
    --deep-top: #23409a;
    --deep-mid: #233888;
    --deep-low: #2a4aa2;
    --rim: #2b4596;
    --ink: #ffffff;
  }
  html, body {
    margin: 0;
    padding: 0;
    width: 1200px;
    height: 1200px;
    overflow: hidden;
    background: var(--page);
  }
  .canvas {
    position: relative;
    width: 1200px;
    height: 1200px;
    font-family: "Inter", Arial, sans-serif;
    color: var(--ink);
  }
  .cap-label {
    position: absolute;
    inset: 0;
  }
  .sub-brand {
    font-family: "Inter", Arial, sans-serif;
    font-size: 31px;
    font-weight: 400;
    letter-spacing: 15px;
    fill: var(--ink);
  }
  .label-copy {
    position: absolute;
    left: 0;
    width: 1200px;
    text-align: center;
    margin: 0;
    line-height: 1;
  }
  .brand-name {
    top: 474px;
    font-size: 74px;
    font-weight: 800;
    letter-spacing: 9px;
  }
  .product-title {
    top: 663px;
    font-size: 46px;
    font-weight: 700;
    letter-spacing: 2px;
  }
  .product-title-fr {
    top: 731px;
    font-size: 28px;
    font-weight: 400;
    letter-spacing: 0.5px;
  }
  .scent-name {
    top: 833px;
    font-size: 21px;
    font-weight: 400;
  }
  .heritage-year {
    top: 870px;
    font-size: 19px;
    font-weight: 400;
  }
  .net-weight {
    top: 918px;
    font-size: 20px;
    font-weight: 400;
  }
</style>
</head>
<body>
<main class="canvas">
  <svg class="cap-label" viewBox="0 0 1200 1200" width="1200" height="1200" aria-hidden="true">
    <defs>
      <linearGradient id="sky-fill" x1="0" y1="0" x2="0" y2="1">
        <stop offset="0" stop-color="var(--sky-top)"/>
        <stop offset="0.55" stop-color="var(--sky-mid)"/>
        <stop offset="1" stop-color="var(--sky-low)"/>
      </linearGradient>
      <linearGradient id="deep-fill" x1="0" y1="0" x2="0" y2="1">
        <stop offset="0" stop-color="var(--deep-top)"/>
        <stop offset="0.5" stop-color="var(--deep-mid)"/>
        <stop offset="1" stop-color="var(--deep-low)"/>
      </linearGradient>
      <clipPath id="disc-clip">
        <circle cx="600" cy="600" r="376"/>
      </clipPath>
      <filter id="soft-glow" x="-20%" y="-50%" width="140%" height="200%">
        <feGaussianBlur stdDeviation="10"/>
      </filter>
      <path id="sub-brand-arc" d="M 104 793 A 496 496 0 0 1 1096 793"/>
    </defs>

    <g clip-path="url(#disc-clip)">
      <rect class="disc-sky" x="200" y="200" width="800" height="800" fill="url(#sky-fill)"/>
      <path class="disc-glow" d="M 200 700 Q 580 520 1000 606" fill="none" stroke="#9aa6e0" stroke-width="22" opacity="0.5" filter="url(#soft-glow)"/>
      <path class="disc-deep" d="M 200 712 Q 580 534 1000 612 L 1000 1000 L 200 1000 Z" fill="url(#deep-fill)"/>
    </g>
    <circle class="disc-rim" cx="600" cy="600" r="376" fill="none" stroke="var(--rim)" stroke-width="1.5"/>

    <text class="sub-brand">
      <textPath href="#sub-brand-arc" startOffset="50%" text-anchor="middle">QUILLSTONE</textPath>
    </text>
  </svg>

  <p class="label-copy brand-name">MARQUEN</p>
  <h1 class="label-copy product-title">SHAVING CREAM</h1>
  <p class="label-copy product-title-fr">CRÈME DE RASAGE</p>
  <p class="label-copy scent-name">HIGHLAND VETIVER</p>
  <p class="label-copy heritage-year">— 1948 —</p>
  <p class="label-copy net-weight">150g e 5.3 oz</p>
</main>
</body>
</html>
```